PixelGuild CEO Needs a Graphic for a Blog About Crowdsourcing and Online Employment

We need a simple graphic / banner for a blog post that's going to be posted on a large publication (like ByteHerald, Marlowe Commerce Quarterly).

The article will be written by Bram Ostiver (PixelGuild's CEO) and the title will be "Why Websites Will Become the Biggest Employers in the World". The article is about why online employers (like PixelGuild and Tasklynx) will one day have more 'workers' than offline employers.

We'd really like to get this ASAP - so early submissions encouraged. We will try and get the winning designer linked to from the article.

Note that this brief is similar to a previous project that we ran http://jobs.pixelguild-example.com/job.aspx?id=58213 where the article and design was published on ByteHerald http://byteherald-example.com/2012/12/08/asias-hidden-gig-surge/ and the designer (Moravia) was linked to from ByteHerald.

Target Market(s)

Entrepreneurs, journalists, small business owners, tech people.

Industry/Entity Type

Business

Requirements
Must have
• The graphic SHOULD have:
1) Have the text "Why Websites Will Become the Biggest Employers in the World" with some nice design and fonts (consider grey subtle pattern background and white drop shadow on fonts) - see attached examples
2) Have the dimensions 640px wide by 240px wide
Nice to have
• The graphic COULD have:

1) Incorporate the following words in the background (like a word cloud): crowdsource, microtask, crowdfund, witkey, outsource, freelance, online, work from home

OR

2) Incorporate logos of new online employers (Tasklynx, vYard, PixelGuild, ChoreFinch, Lunqiaofu, ClockworkPawn, Frameharbor) into the design. If the background of the graphic is grey, ideally, these logos would also be greyscale i.e. they should form a background motif.

OR

3) Show some graphic communicating themes from the article e.g. laptop, globe, workers, connections across the globe

OR

4) Have a second line of text "Why Crowdsourcing Websites Will Overtake Traditional Employers"
Should not have
• Should NOT have:
1) Any photos or clipart

```html
<!DOCTYPE html>
<html lang="en">
<head>
<meta charset="utf-8">
<title>Why Websites Will Become the Biggest Employers in the World</title>
<link rel="stylesheet" href="https://fonts.googleapis.com/css2?family=Questrial&display=swap">
<style>
  :root {
    --ink: #2f2f2f;
    --ink-soft: #3c3c3c;
    --ghost: rgba(40, 40, 40, 0.26);
    --paper: #f4f4f4;
    --mottle: rgba(150, 150, 150, 0.22);
    --tasklynx-tile: #ffffff;
    --tasklynx-ink: #e4734a;
    --chorefinch-tile: #3f9e6c;
    --vyard-tile: #8cc06a;
    --tile-ink: #ffffff;
    --faint-blue: rgba(70, 140, 200, 0.35);
  }
  html, body {
    margin: 0;
    padding: 0;
    overflow: hidden;
    background: #ffffff;
  }
  .banner {
    position: relative;
    width: 1200px;
    height: 450px;
    overflow: hidden;
    font-family: "Questrial", sans-serif;
    background:
      radial-gradient(ellipse 260px 140px at 230px 380px, var(--mottle), transparent 70%),
      radial-gradient(ellipse 200px 120px at 560px 430px, var(--mottle), transparent 70%),
      radial-gradient(ellipse 300px 160px at 680px 120px, rgba(150,150,150,0.18), transparent 70%),
      radial-gradient(ellipse 220px 200px at 80px 60px, rgba(160,160,160,0.16), transparent 70%),
      radial-gradient(ellipse 420px 240px at 300px 220px, #ffffff, transparent 75%),
      var(--paper);
  }
  .tile {
    position: absolute;
    display: flex;
    align-items: center;
    justify-content: center;
  }
  .tile-faded {
    left: 690px;
    top: 190px;
    width: 150px;
    height: 150px;
    background: rgba(200, 200, 200, 0.35);
    filter: blur(6px);
  }
  .tile-tasklynx {
    left: 740px;
    top: 9px;
    width: 197px;
    height: 179px;
    background: var(--tasklynx-tile);
    opacity: 0.92;
    box-shadow: 0 0 18px rgba(255,255,255,0.9);
  }
  .tile-tasklynx .name {
    font-size: 28px;
    color: var(--tasklynx-ink);
  }
  .tile-chorefinch {
    left: 950px;
    top: 9px;
    width: 171px;
    height: 179px;
    background: var(--chorefinch-tile);
  }
  .tile-chorefinch .name {
    font-size: 28px;
    color: var(--tile-ink);
  }
  .tile-vyard {
    left: 834px;
    top: 197px;
    width: 366px;
    height: 253px;
    background: var(--vyard-tile);
  }
  .tile-vyard .name {
    font-size: 40px;
    color: var(--tile-ink);
  }
  .faint-dot {
    position: absolute;
    left: 655px;
    top: 325px;
    width: 80px;
    height: 80px;
    border-radius: 50%;
    background: var(--faint-blue);
    filter: blur(1px);
  }
  .headline {
    position: absolute;
    z-index: 2;
    left: 47px;
    top: 58px;
    margin: 0;
    font-weight: 400;
    font-size: 53px;
    line-height: 81px;
    color: var(--ink);
    white-space: nowrap;
    text-shadow: 0 32px 5px var(--ghost);
  }
  .subline {
    position: absolute;
    z-index: 2;
    left: 116px;
    top: 239px;
    margin: 0;
    font-weight: 400;
    font-size: 31px;
    line-height: 71px;
    color: var(--ink-soft);
    white-space: nowrap;
    text-shadow: 0 20px 4px rgba(40, 40, 40, 0.2);
  }
</style>
</head>
<body>
  <main class="banner">
    <div class="tile tile-faded" aria-hidden="true"></div>
    <div class="faint-dot" aria-hidden="true"></div>

    <div class="tile tile-tasklynx"><span class="name">Tasklynx</span></div>
    <div class="tile tile-chorefinch"><span class="name">ChoreFinch</span></div>
    <div class="tile tile-vyard"><span class="name">vYard</span></div>

    <h1 class="headline">Why Websites Will Become<br>the Biggest Employers in the World</h1>
    <p class="subline">Why Crowdsourcing Websites Will Overtake<br>Traditional Employers</p>
  </main>
</body>
</html>
```